Need FaceBook, Linkedin, Instagram, Twitter banners designed

We need to have the logos ovantri wallet logo, and the TallyBloom a service of ovantri Logo. Both attached herein. turned into Social Media Banners. (FaceBook, LinkedIn, Instagram, Twitter). Different Banners for each of the two logos for each of the 4 media outlets:
1) ovantri - Just the wallet
2) TallyBloom

```html
<!DOCTYPE html>
<html lang="en">
<head>
<meta charset="utf-8">
<title>TallyBloom social banners</title>
<link rel="stylesheet" href="https://fonts.googleapis.com/css2?family=Didact+Gothic&family=Poppins:wght@500&display=swap">
<style>
  :root {
    --board: #2d2d2d;
    --label: #ffffff;
    --banner: #ffffff;
    --ink: #1c1c1c;
    --accent: #ef6a24;
    --swoosh: #b8b8b8;
    --swoosh-light: #dcdcdc;
    --wallet-dark: #3a3536;
    --wallet-mid: #5b5354;
  }
  * { box-sizing: border-box; margin: 0; padding: 0; }
  html, body { width: 1200px; height: 1000px; overflow: hidden; background: var(--board); }
  .board { position: relative; width: 1200px; height: 1000px; background: var(--board); }
  .size-label {
    position: absolute; transform: translateX(-50%);
    font-family: "Poppins", sans-serif; font-weight: 500; font-size: 19px;
    color: var(--label); white-space: nowrap;
  }
  .banner { position: absolute; background: var(--banner); overflow: hidden; }
  .banner svg.backdrop { position: absolute; inset: 0; width: 100%; height: 100%; }
  .brand { position: absolute; display: flex; align-items: center; }
  .brand-dot { border-radius: 50%; background: var(--accent); flex: none; }
  .brand-name {
    font-family: "Didact Gothic", sans-serif; color: var(--ink);
    line-height: 1; white-space: nowrap;
  }
  .wallet {
    position: absolute; border-radius: 6px;
    background: linear-gradient(160deg, #b3262f 0%, #6b2a58 10%, var(--wallet-mid) 14%, var(--wallet-dark) 100%);
    box-shadow: 0 4px 10px rgba(0,0,0,.35);
  }
</style>
</head>
<body>
<main class="board">
  <defs-holder>
  <svg width="0" height="0" style="position:absolute">
    <defs>
      <linearGradient id="mosaic-tones" x1="0" y1="0" x2="1" y2="1">
        <stop offset="0" stop-color="#2fa9e0"/>
        <stop offset=".3" stop-color="#f6d21b"/>
        <stop offset=".55" stop-color="#e83a7a"/>
        <stop offset=".8" stop-color="#f08a24"/>
        <stop offset="1" stop-color="#3bb54a"/>
      </linearGradient>
    </defs>
  </svg>
  </defs-holder>

  <!-- 1584 x 396 -->
  <p class="size-label" style="left:600px;top:40px">1584 x 396</p>
  <section class="banner" style="left:41px;top:78px;width:1125px;height:281px">
    <svg class="backdrop" viewBox="0 0 1125 281" preserveAspectRatio="none">
      <path d="M0 230 C250 180 500 240 760 190 C900 165 1000 200 1125 180" fill="none" stroke="var(--swoosh)" stroke-width="14"/>
      <path d="M0 265 C300 220 560 270 820 230 C950 212 1050 240 1125 225" fill="none" stroke="var(--swoosh-light)" stroke-width="10"/>
      <path d="M1125 0 L1125 281 L945 281 C990 230 1030 150 1060 60 C1075 30 1095 10 1125 0 Z" fill="url(#mosaic-tones)" role="img" aria-label="Colourful diamond mosaic pattern"/>
    </svg>
    <div class="brand" style="left:70px;top:36px;gap:26px">
      <span class="brand-dot" style="width:58px;height:58px"></span>
      <span class="brand-name" style="font-size:84px">TallyBloom</span>
    </div>
    <div class="wallet" role="img" aria-label="Dark wallet illustration with the ovantri name" style="left:824px;top:14px;width:236px;height:216px"></div>
  </section>

  <!-- 1080 x 1080 -->
  <p class="size-label" style="left:270px;top:400px">1080 x 1080</p>
  <section class="banner" style="left:41px;top:452px;width:469px;height:469px">
    <svg class="backdrop" viewBox="0 0 469 469" preserveAspectRatio="none">
      <path d="M0 250 C120 200 260 170 469 175" fill="none" stroke="var(--swoosh)" stroke-width="12"/>
      <path d="M0 280 C140 230 300 200 469 220" fill="none" stroke="var(--swoosh-light)" stroke-width="8"/>
      <path d="M0 260 C90 230 200 210 300 225 L290 280 L240 469 L0 469 Z" fill="url(#mosaic-tones)" role="img" aria-label="Colourful diamond mosaic pattern"/>
    </svg>
    <div class="brand" style="left:30px;top:56px;gap:14px">
      <span class="brand-dot" style="width:34px;height:34px"></span>
      <span class="brand-name" style="font-size:50px">TallyBloom</span>
    </div>
    <div class="wallet" role="img" aria-label="Dark wallet illustration with the ovantri name" style="left:233px;top:250px;width:216px;height:200px"></div>
  </section>

  <!-- 820 x 312 -->
  <p class="size-label" style="left:848px;top:400px">820 x 312</p>
  <section class="banner" style="left:557px;top:452px;width:596px;height:225px">
    <svg class="backdrop" viewBox="0 0 596 225" preserveAspectRatio="none">
      <path d="M0 130 C150 170 330 150 596 200" fill="none" stroke="var(--swoosh)" stroke-width="10"/>
      <path d="M0 160 C180 190 380 170 596 215" fill="none" stroke="var(--swoosh-light)" stroke-width="7"/>
      <path d="M460 0 L596 0 L596 200 C560 170 520 110 490 60 C478 40 468 20 460 0 Z" fill="url(#mosaic-tones)" role="img" aria-label="Colourful diamond mosaic pattern"/>
    </svg>
    <div class="brand" style="left:18px;top:22px;gap:16px">
      <span class="brand-dot" style="width:40px;height:40px"></span>
      <span class="brand-name" style="font-size:56px">TallyBloom</span>
    </div>
    <div class="wallet" role="img" aria-label="Dark wallet illustration with the ovantri name" style="left:316px;top:120px;width:114px;height:92px"></div>
  </section>

  <!-- 1500 x 500 -->
  <section class="banner" style="left:557px;top:719px;width:594px;height:197px">
    <svg class="backdrop" viewBox="0 0 594 197" preserveAspectRatio="none">
      <path d="M0 140 C160 100 360 130 594 110" fill="none" stroke="var(--swoosh)" stroke-width="10"/>
      <path d="M0 175 C200 135 400 160 594 140" fill="none" stroke="var(--swoosh-light)" stroke-width="7"/>
      <path d="M594 0 L594 197 L470 197 C510 160 550 90 575 30 C582 15 588 6 594 0 Z" fill="url(#mosaic-tones)" role="img" aria-label="Colourful diamond mosaic pattern"/>
    </svg>
    <div class="brand" style="left:20px;top:26px;gap:16px">
      <span class="brand-dot" style="width:38px;height:38px"></span>
      <span class="brand-name" style="font-size:50px">TallyBloom</span>
    </div>
    <div class="wallet" role="img" aria-label="Dark wallet illustration with the ovantri name" style="left:402px;top:14px;width:130px;height:123px"></div>
  </section>
  <p class="size-label" style="left:871px;top:951px">1500 x 500</p>
</main>
</body>
</html>
```